Website and Mobile Devices design for food related application.

We need a design that is simple yet playful. The design should be food related if possible.
This design will be on the website and the mobile platform markets we intend application to be deployed too.
This application/website is called "Pickvoro[.com]. Its a random restaurant picker for the indecisive users.
Updates
Hi all, I picked a design. Again lots of great designs were submitted but I picked one that was more in line with what I wanted.
Target Market(s)
young internet savvy users.
Industry/Entity Type
Restaurant
Look and feel
Each slider illustrates characteristics of the customer's brand and the style your logo design should communicate.

```html
<!DOCTYPE html>
<html lang="en">
<head>
<meta charset="utf-8">
<title>Pickvoro – Random Restaurant Picker</title>
<link href="https://fonts.googleapis.com/css2?family=Cinzel:wght@400&family=Ubuntu:wght@400;500;700&family=Cuprum:wght@400;700&family=Lora:ital@1&display=swap" rel="stylesheet">
<style>
:root{
  --red:#d9261c;
  --red-dark:#b5170f;
  --text:#5c5c5c;
  --heading:#444;
  --muted:#777;
  --line:#dcdcdc;
  --page:#ffffff;
  --band:#e4e4e4;
}
*{margin:0;padding:0;box-sizing:border-box}
html,body{width:986px;height:1200px;overflow:hidden;background:var(--page)}
body{position:relative;font-family:"Cuprum",sans-serif;color:var(--text)}
.abs{position:absolute}

.site-header{left:0;top:0;width:986px;height:116px;background:linear-gradient(#fff,#f3f3f3);border-bottom:1px solid #d8d8d8}
.tagline{left:30px;top:40px;font:400 9px "Ubuntu",sans-serif;color:#444;letter-spacing:.2px}
.brand{left:30px;top:50px;font:400 52px/1 "Cinzel",serif;color:var(--red)}
.cart{right:30px;top:28px;display:flex;align-items:center;gap:10px;font:400 11px "Ubuntu",sans-serif;color:#666}
.cart .sep{margin:0 6px}
.main-nav{right:8px;top:92px;display:flex;font:500 13px "Ubuntu",sans-serif}
.main-nav a{color:var(--red);text-decoration:none;padding:0 15px;border-left:1px solid #e2e2e2}
.main-nav a:first-child{border-left:none;color:#444}

.band{left:0;top:117px;width:986px;height:485px;background:linear-gradient(var(--band),#f6f6f6 60%,#fff)}
.hero{left:30px;top:158px;width:926px;height:365px;background:#fff;border:1px solid var(--line);padding:7px}
.hero-art{width:100%;height:100%;background:radial-gradient(ellipse at 55% 60%,#c23d22 0%,#7a8a2a 30%,#5a5a30 60%,#3b3520 100%)}

.card{top:563px;width:304px;height:307px;background:linear-gradient(#fff,#f5f5f5);border:1px solid var(--line)}
.ribbon{left:-9px;top:19px;width:280px;height:39px;background:linear-gradient(var(--red),var(--red-dark));color:#fff;font:400 14px/39px "Cinzel",serif;padding-left:28px;letter-spacing:.3px}
.card h2{position:absolute;left:19px;top:71px;font:500 16px "Ubuntu",sans-serif;color:var(--heading)}
.card p{position:absolute;left:19px;top:108px;width:240px;font:400 14px/20.3px "Cuprum",sans-serif;color:var(--text)}
.read-more{position:absolute;left:19px;top:261px;width:160px;height:32px;border:1px solid #c8c8c8;border-radius:16px;background:linear-gradient(#fff,#efefef);font:italic 18px/30px "Lora",serif;color:#777;text-align:center}

.site-footer{left:30px;top:911px;width:926px;height:270px;background:linear-gradient(#f3f3f3,#fff);border:1px solid var(--line)}
.f-col{top:22px;width:200px}
.f-col h3{font:500 14px "Ubuntu",sans-serif;color:var(--red);margin-bottom:15px}
.f-col li{list-style:none;font:400 13px/19.5px "Cuprum",sans-serif;color:var(--muted)}
.hours{font:400 13px/19.5px "Cuprum",sans-serif;color:var(--muted)}
.hours b{color:#555}
.accept{left:45px;top:185px}
.accept h3{font:500 14px "Ubuntu",sans-serif;color:var(--red);margin-bottom:14px}
.pay{display:flex;gap:10px}
.pay span{width:64px;height:40px;border-radius:3px;font:700 11px/40px "Ubuntu",sans-serif;color:#fff;text-align:center}
</style>
</head>
<body>
<header class="abs site-header">
  <div class="abs tagline">RANDOM RESTAURANT PICKER</div>
  <div class="abs brand">Pickvoro</div>
  <div class="abs cart">
    <svg width="24" height="18" viewBox="0 0 24 18" aria-hidden="true"><path d="M1 2h4l3 10h11l3-7H7" fill="none" stroke="#777" stroke-width="1.5"/><circle cx="10" cy="15.5" r="1.5" fill="#777"/><circle cx="18" cy="15.5" r="1.5" fill="#777"/></svg>
    <span>Shopping Cart</span><span class="sep">|</span><span>(0) Items</span>
  </div>
  <nav class="abs main-nav"><a href="#">Home</a><a href="#">Cuisines</a><a href="#">Ingredients</a><a href="#">New Restaurants</a><a href="#">Contact</a></nav>
</header>

<div class="abs band"></div>
<section class="abs hero"><div class="hero-art" role="img" aria-label="Photo of fresh vegetables, herbs, lemon, garlic and a bottle of olive oil"></div></section>

<article class="abs card" style="left:30px">
  <div class="abs ribbon">CAUSAE APPETERE SENSIBUS</div>
  <h2>Appareat Urbanitas</h2>
  <p>Numquam adolescens persequeris sea an. In eros nusquam intellegam usu, te sit menandri intellegam. Cu his duis eruditi hendrerit, novum exerci accusata cu eos. An enim viderer vis, eum quas mutat animal cu, te eum partem tempor consequat. Sit debitis voluptaria</p>
  <div class="read-more">Read more</div>
</article>
<article class="abs card" style="left:341px">
  <div class="abs ribbon">CAUSAE APPETERE SENSIBUS</div>
  <h2>Appareat Urbanitas</h2>
  <p>Numquam adolescens persequeris sea an. In eros nusquam intellegam usu, te sit menandri intellegam. Cu his duis eruditi hendrerit, novum exerci accusata cu eos. An enim viderer vis, eum quas mutat animal cu, te eum partem tempor consequat. Sit debitis voluptaria</p>
  <div class="read-more">Read more</div>
</article>
<article class="abs card" style="left:652px">
  <div class="abs ribbon">CAUSAE APPETERE SENSIBUS</div>
  <h2>Appareat Urbanitas</h2>
  <p>Numquam adolescens persequeris sea an. In eros nusquam intellegam usu, te sit menandri intellegam. Cu his duis eruditi hendrerit, novum exerci accusata cu eos. An enim viderer vis, eum quas mutat animal cu, te eum partem tempor consequat. Sit debitis voluptaria</p>
  <div class="read-more">Read more</div>
</article>

<footer class="abs site-footer">
  <div class="abs f-col" style="left:45px"><h3>Gloriatur Dicam</h3><ul><li>Reformidans luvaret</li><li>Consequuntur</li><li>Ullamcorper Essent</li><li>Gloriatur Dicam</li><li>Primis Scriptorem</li></ul></div>
  <div class="abs f-col" style="left:285px"><h3>Gloriatur Dicam</h3><ul><li>Reformidans luvaret</li><li>Consequuntur</li><li>Ullamcorper Essent</li><li>Gloriatur Dicam</li><li>Primis Scriptorem</li></ul></div>
  <div class="abs f-col" style="left:525px"><h3>Gloriatur Dicam</h3><ul><li>Reformidans luvaret</li><li>Consequuntur</li><li>Ullamcorper Essent</li><li>Gloriatur Dicam</li><li>Primis Scriptorem</li><li>Nulla Dolore Aliquando</li><li>Reformidans luvaret</li></ul></div>
  <div class="abs f-col" style="left:764px"><h3>Opening Hours</h3>
    <div class="hours"><b>Mon- Sat:</b>&nbsp; 00am - 00pm<br><b>Sunday:</b>&nbsp; 00am - 00pm</div>
    <div class="hours" style="margin-top:16px">1234 Street Name<br>City Name<br>ZIP 1234<br>email@example.com</div>
  </div>
  <div class="abs accept"><h3>We Accept</h3>
    <div class="pay"><span style="background:#9a9a9a">Tendro</span><span style="background:#1a4f9c">Paynest</span><span style="background:#d9a640">Coinvale</span><span style="background:#1d3b86">Credora</span><span style="background:#3a4ea0">Swiftab</span></div>
  </div>
</footer>
</body>
</html>
```